Landing Page für Kornwiese-Prüfset.de
Zielgruppe
Domain: Kornwiese-Prüfset.de
THC Schnelltests mit gringer Anzeigegrenze mit 5ng/ml, ausgerichtet auf die Selbstkontrolle für die Fahrtauglichkeit (Grenze im Gesetz 3,5ng/ml)
Farbe: grün
Anregung siehe Bild
Aufgabenstellung
- Conversionoptimiert
- Soll auf unseren Webshop www.rv-vitalis.de verlinken

```html
<!DOCTYPE html>
<html lang="de">
<head>
<meta charset="utf-8">
<title>Kornwiese-Prüfset.de – Mach den Selbsttest</title>
<link rel="stylesheet" href="https://fonts.googleapis.com/css2?family=Jost:wght@400;500&family=Montserrat:wght@700&display=swap">
<style>
  :root {
    --ink: #111a13;
    --paper: #ffffff;
    --hero-dark: #0c1a10;
    --hero-green: #2f6b3a;
    --hero-glow: #b9d99a;
    --accent: #2e7d3a;
    --accent-dark: #1f5a29;
    --nav-glass: rgba(255, 255, 255, 0.12);
    --muted-text: #1d261f;
  }
  * { box-sizing: border-box; margin: 0; padding: 0; }
  html, body { width: 1200px; height: 753px; overflow: hidden; background: var(--paper); }
  body { font-family: "Jost", sans-serif; color: var(--ink); position: relative; }

  .hero {
    position: absolute; left: 0; top: 0; width: 1200px; height: 526px;
    border-radius: 0 0 14px 14px; overflow: hidden;
  }
  .hero-photo {
    position: absolute; inset: 0;
    background:
      radial-gradient(ellipse 55% 45% at 70% 28%, var(--hero-glow) 0%, rgba(185,217,154,0) 70%),
      radial-gradient(ellipse 40% 50% at 22% 30%, var(--hero-green) 0%, rgba(47,107,58,0) 75%),
      linear-gradient(180deg, #2b5a31 0%, #173520 55%, var(--hero-dark) 100%);
  }
  .hero-shade {
    position: absolute; inset: 0;
    background: linear-gradient(90deg, rgba(0,0,0,0.35) 0%, rgba(0,0,0,0.05) 60%, rgba(0,0,0,0.2) 100%);
  }

  .site-nav {
    position: absolute; left: 126px; top: 39px; width: 947px; height: 65px;
    border-radius: 8px; background: var(--nav-glass);
  }
  .brand {
    position: absolute; left: 21px; top: 18px;
    font-weight: 500; font-size: 21px; color: var(--paper); letter-spacing: 0.5px;
  }
  .nav-link {
    position: absolute; top: 20px; height: 28px; line-height: 28px;
    font-size: 11.5px; color: var(--paper); text-decoration: none; text-align: center; white-space: nowrap;
  }
  .nav-link.is-active { background: var(--paper); color: var(--ink); border-radius: 5px; left: 569px; width: 57px; }
  .nav-link.solution { left: 644px; width: 90px; }
  .nav-link.faq { left: 757px; width: 30px; }
  .nav-cta { background: var(--accent); border-radius: 5px; left: 818px; width: 91px; }

  .hero-copy { position: absolute; left: 155px; top: 295px; color: var(--paper); }
  .tag {
    display: inline-block; background: var(--paper); color: var(--accent-dark);
    font-size: 7px; padding: 3px 7px; border-radius: 9px;
  }
  .headline {
    font-family: "Montserrat", sans-serif; font-weight: 700;
    font-size: 34px; margin-top: 6px; line-height: 1.1; white-space: nowrap;
  }
  .subline { font-size: 14.5px; margin-top: 6px; }
  .hero-cta {
    display: inline-block; margin-top: 13px; background: var(--paper); color: var(--accent-dark);
    font-size: 11.5px; text-decoration: none; padding: 7px 15px; border-radius: 5px;
  }

  .benefits { position: absolute; top: 580px; left: 0; width: 1200px; }
  .benefit { position: absolute; width: 290px; text-align: center; transform: translateX(-50%); }
  .benefit svg { width: 34px; height: 34px; display: block; margin: 0 auto; }
  .benefit h2 { font-weight: 500; font-size: 19px; margin-top: 8px; letter-spacing: 0.3px; color: var(--ink); }
  .benefit p { font-size: 12.5px; line-height: 20px; margin-top: 2px; color: var(--muted-text); }
  .b-fast { left: 273px; }
  .b-precise { left: 599px; }
  .b-easy { left: 918px; }
</style>
</head>
<body>
  <header class="hero">
    <div class="hero-photo" role="img" aria-label="Grün getöntes Foto: Person am Steuer eines Autos, Blick durch die Windschutzscheibe"></div>
    <div class="hero-shade"></div>

    <nav class="site-nav">
      <div class="brand">RV Vitalis</div>
      <a class="nav-link is-active" href="#">Start</a>
      <a class="nav-link solution" href="#">Unsere Lösung</a>
      <a class="nav-link faq" href="#">FAQ</a>
      <a class="nav-link nav-cta" href="https://www.rv-vitalis.de">Jetzt kaufen</a>
    </nav>

    <div class="hero-copy">
      <span class="tag">THC-Schnelltest</span>
      <h1 class="headline">MACH DEN SELBSTTEST.</h1>
      <p class="subline">Gefährde nicht deinen Führerschein!</p>
      <a class="hero-cta" href="https://www.rv-vitalis.de">Jetzt kaufen</a>
    </div>
  </header>

  <section class="benefits">
    <div class="benefit b-fast">
      <svg viewBox="0 0 24 24" aria-hidden="true"><path d="M14 1 5 14h6l-2 9 9-13h-6z" fill="#2e7d3a"/></svg>
      <h2>SCHNELL</h2>
      <p>Ergebnisse in wenigen Minuten sofortige<br>Sicherheit für Ihre Fahrtüchtigkeit.</p>
    </div>
    <div class="benefit b-precise">
      <svg viewBox="0 0 24 24" aria-hidden="true" stroke="#2e7d3a" stroke-width="2.2" stroke-linecap="round">
        <line x1="12" y1="2" x2="12" y2="7"/><line x1="12" y1="17" x2="12" y2="22"/>
        <line x1="2" y1="12" x2="7" y2="12"/><line x1="17" y1="12" x2="22" y2="12"/>
        <circle cx="12" cy="12" r="1.6" fill="#2e7d3a" stroke="none"/>
      </svg>
      <h2>PRÄZISE</h2>
      <p>Genaue Messung mit einer Anzeigegrenze<br>von 5ng/ml für verlässliche Ergebnisse.</p>
    </div>
    <div class="benefit b-easy">
      <svg viewBox="0 0 24 24" aria-hidden="true"><path d="M2 10h4v12H2zM8 10l5-8c2 0 3 1 2.5 3L14 9h6c1.5 0 2.3 1.3 2 2.6l-2 8.4c-.3 1.2-1.2 2-2.4 2H8z" fill="#2e7d3a"/></svg>
      <h2>EINFACH</h2>
      <p>Einfache Anwendung, die jeder<br>problemlos zu Hause durchführen kann.</p>
    </div>
  </section>
</body>
</html>
```